Realtor resource

This is a website that provides resources for Realtors and their customers (home buyers and sellers).

There are 5 pages that I need redesigned:

1. Homepage: https://brightkeyguide.example/
2. Support Page/Contact Us: https://brightkeyguide.example/contact-us/
3. Agent Dashboard - See attached screenshot
4. Real Estate Documents page - See attached screenshot
5. Real Estate Contract page - see attached screenshot

Target Market(s)

Real estate agents and their customers.

Industry/Entity Type

Real Estate

Number of Pages Required

5+ page

Requirements
Must have
• Please use a modern design and incorporate design with current logo.

```html
<!DOCTYPE html>
<html lang="en">
<head>
<meta charset="utf-8">
<title>BrightKeyGuide – Real Estate Contracts</title>
<link rel="stylesheet" href="https://fonts.googleapis.com/css2?family=Oswald:wght@600&family=Poppins:wght@400;500;600;800&display=swap">
<style>
  :root {
    --orange-deep: #f7941d;
    --orange-bright: #fdb813;
    --orange-brand: #f5a01a;
    --ink: #1c1c1c;
    --muted-brown: #9a5f17;
    --white: #ffffff;
    --line: #555555;
  }
  * { box-sizing: border-box; margin: 0; padding: 0; }
  html, body { width: 1200px; height: 712px; overflow: hidden; }
  body { position: relative; font-family: "Poppins", sans-serif; color: var(--ink); background: var(--white); }

  .site-header { position: absolute; left: 0; top: 0; width: 1200px; height: 94px; background: var(--white); }
  .brand { position: absolute; left: 36px; top: 30px; text-decoration: none; }
  .brand-name { font-size: 27px; font-weight: 600; color: var(--ink); letter-spacing: -0.5px; }

  .search { position: absolute; left: 494px; top: 35px; width: 195px; height: 24px; border: 1.5px solid var(--line); border-radius: 14px; }
  .search svg { position: absolute; right: 9px; top: 4px; }

  .main-nav { position: absolute; left: 721px; top: 39px; display: flex; font-size: 10.5px; color: var(--ink); }
  .main-nav a { color: inherit; text-decoration: none; }
  .main-nav .sep { margin: 0 14px; }

  .signup-btn { position: absolute; left: 1087px; top: 32px; width: 79px; height: 30px; border-radius: 15px; background: var(--orange-brand); color: var(--white); font-size: 10.5px; font-weight: 500; display: flex; align-items: center; justify-content: center; text-decoration: none; }

  .hero { position: absolute; left: 0; top: 94px; width: 1200px; height: 558px; background: linear-gradient(125deg, var(--orange-deep) 0%, var(--orange-bright) 100%); }
  .hero-title { position: absolute; left: 157px; top: 140px; font-family: "Oswald", sans-serif; font-weight: 600; font-size: 57px; line-height: 63px; letter-spacing: 5px; color: var(--white); }
  .hero-lead { position: absolute; left: 161px; top: 275px; font-size: 23px; font-weight: 500; color: var(--white); }
  .hero-byline { position: absolute; left: 159px; top: 318px; font-size: 14px; font-weight: 500; letter-spacing: 0.8px; color: var(--muted-brown); }
  .updates-label { position: absolute; left: 160px; top: 374px; font-size: 14px; font-weight: 600; letter-spacing: 0.8px; color: var(--white); }
  .email-field { position: absolute; left: 160px; top: 409px; width: 299px; height: 31px; border-radius: 16px; background: var(--white); font-size: 9px; color: #9a9a9a; padding-left: 14px; display: flex; align-items: center; }
  .submit-btn { position: absolute; left: 469px; top: 409px; width: 88px; height: 31px; border-radius: 16px; background: var(--white); color: var(--orange-brand); font-size: 10px; font-weight: 600; letter-spacing: 0.5px; display: flex; align-items: center; justify-content: center; }

  .audience { position: absolute; left: 0; top: 0; }
  .audience text { font-family: "Poppins", sans-serif; font-weight: 800; font-size: 21px; fill: var(--ink); text-anchor: middle; }

  .site-footer { position: absolute; left: 0; top: 652px; width: 1200px; height: 60px; background: var(--white); font-size: 9.5px; color: var(--ink); }
  .footer-legal { position: absolute; left: 164px; top: 11px; }
  .footer-legal a { color: inherit; text-decoration: none; }
  .footer-contact { position: absolute; left: 553px; top: 11px; display: flex; align-items: center; gap: 6px; }
  .footer-social { position: absolute; left: 974px; top: 13px; display: flex; gap: 13px; }
  .footer-social span { width: 10px; height: 10px; border-radius: 50%; background: #2b2b3a; }
</style>
</head>
<body>
  <header class="site-header">
    <a class="brand" href="https://brightkeyguide.example/">
      <span class="brand-name">BrightKeyGuide</span>
    </a>
    <div class="search">
      <svg width="12" height="12" viewBox="0 0 12 12"><circle cx="5" cy="5" r="3.8" fill="none" stroke="#555" stroke-width="1.6"/><line x1="7.8" y1="7.8" x2="11" y2="11" stroke="#555" stroke-width="1.6" stroke-linecap="round"/></svg>
    </div>
    <nav class="main-nav">
      <a href="https://brightkeyguide.example/">Home</a><span class="sep">-</span>
      <a href="https://brightkeyguide.example/contact-us/">Support</a><span class="sep">-</span>
      <a href="#">Real Estate Documents</a><span class="sep">-</span>
      <a href="https://brightkeyguide.example/contact-us/">Contact</a>
    </nav>
    <a class="signup-btn" href="#">SIGNUP</a>
  </header>

  <section class="hero">
    <h1 class="hero-title">REAL ESTATE<br>CONTRACTS</h1>
    <p class="hero-lead">Explained in plain language</p>
    <p class="hero-byline">BY TEXAS REAL ESTATE ATTORNEYS.</p>
    <p class="updates-label">SIGN UP FOR UPDATES</p>
    <div class="email-field">Type your email id</div>
    <div class="submit-btn">SUBMIT</div>
  </section>

  <svg class="audience" width="1200" height="712" viewBox="0 0 1200 712">
    <defs>
      <linearGradient id="keysTone" x1="0" y1="0" x2="1" y2="1">
        <stop offset="0" stop-color="#d9dde2"/><stop offset="1" stop-color="#eef0f2"/>
      </linearGradient>
      <linearGradient id="cityTone" x1="0" y1="0" x2="0" y2="1">
        <stop offset="0" stop-color="#d6d6d6"/><stop offset="0.5" stop-color="#9a9a9a"/><stop offset="1" stop-color="#4a4a4a"/>
      </linearGradient>
    </defs>
    <polygon points="714,135 848,203 848,337 714,402 581,337 581,203" fill="none" stroke="#fff" stroke-width="6"/>
    <polygon role="img" aria-label="Photo of a hand holding out car keys" points="714,147 838,210 838,331 714,391 591,331 591,210" fill="url(#keysTone)"/>
    <polygon points="850,343 985,410 985,542 850,611 717,542 717,410" fill="none" stroke="#fff" stroke-width="6"/>
    <polygon role="img" aria-label="Black and white photo of a city skyline under clouds" points="850,355 975,417 975,535 850,599 727,535 727,417" fill="url(#cityTone)"/>
    <text x="654" y="270">BUYERS</text>
    <text x="655" y="297">&amp; SELLERS</text>
    <text x="850" y="426">AGENTS</text>
  </svg>

  <footer class="site-footer">
    <p class="footer-legal">© Copyright 2019. All Rights Reserved. &nbsp;| &nbsp; <a href="https://brightkeyguide.example/contact-us/">Contact Us</a></p>
    <p class="footer-contact">
      <svg width="8" height="8" viewBox="0 0 10 10"><path d="M2 0.5 L3.8 2.8 L2.8 4 Q4 6.2 6 7.2 L7.2 6.2 L9.5 8 L8.2 9.5 Q3.5 9 0.5 1.8 Z" fill="#222"/></svg>
      <span>1800 555 0147</span>
      <span style="margin:0 10px">|</span>
      <svg width="9" height="7" viewBox="0 0 9 7"><rect width="9" height="7" rx="1" fill="#222"/><path d="M0.5 0.8 L4.5 3.8 L8.5 0.8" fill="none" stroke="#fff" stroke-width="0.9"/></svg>
      <span>info@brightkeyguide.example</span>
    </p>
    <div class="footer-social" aria-label="Social links">
      <span></span><span></span><span></span>
    </div>
  </footer>
</body>
</html>
```